Flyer für Vermietung von Autos und Mietkauf
Zielgruppe
Vermietung von Autos und Mietkauf Lösungen
Aufgabenstellung
Wichtig ist dass die Farben unserer CI benutzt werden. Am Besten an www.pk-mobil.de orientieren. Der Flyer soll eine kurze Vorstellung des Mietkauf Modells sein.
Es geht um folgendes:
Kunden haben die Möglichkeit über uns Autos zu 'finanzieren' (Mietkauf). Der Kunde kann sich ein beliebiges Fahrzeug im Netz aussuchen (muss MwSt haben) und über uns mietkaufen. Er muss 35% des Fahrzeugpreises anbezahlen und der Vertrag läuft 2 Jahre. Danach kann er das Fahrzeug zum Restwert rauskaufen. Das ganze ohne Bonitätsprüfung und KREVAG. Es soll ein informatives PDF sein, welches ich potentiellen Kunden per Mail oder WhatsApp schicke. Es geht primär um Luxusfahrzeuge wie Veltrano RSXs oder auch Castellaris. Das Design sollte also daran angelehnt sein.

```html
<!DOCTYPE html>
<html lang="de">
<head>
<meta charset="utf-8">
<title>Veloura Cars – Flyer Mietkauf</title>
<link href="https://fonts.googleapis.com/css2?family=Lato:wght@300;400;700;900&display=swap" rel="stylesheet">
<style>
  :root{
    --gold:#c9b574;
    --ink:#1b1b1b;
    --paper:#ebebea;
    --stage:#f3f2f0;
    --white:#ffffff;
  }
  *{box-sizing:border-box;margin:0;padding:0}
  html,body{width:718px;height:1200px;overflow:hidden;background:var(--stage);font-family:"Lato",sans-serif;color:var(--ink)}
  .page{position:absolute;width:320px;height:452px;overflow:hidden;box-shadow:0 2px 8px rgba(0,0,0,.12)}
  .page--cover{left:26px;top:90px;background:var(--gold)}
  .page--info{left:372px;top:90px;background:var(--paper)}
  .page--contact{left:199px;top:610px;background:var(--paper)}
  .abs{position:absolute}

  .hero-photo{position:absolute;left:0;top:0;width:320px;height:323px;
    background:
      radial-gradient(ellipse 90px 40px at 60px 200px, rgba(230,235,238,.85), transparent 70%),
      radial-gradient(ellipse 70px 22px at 200px 180px, #3a3f47, transparent 75%),
      linear-gradient(180deg,#2f3a24 0%,#4d5d33 35%,#3c4a40 60%,#5f6e3c 85%,#a79d54 100%);
    clip-path:polygon(0 0,100% 0,100% 276px,0 323px)}

  .brand{position:absolute;left:25px;top:24px;width:108px;height:87px;background:var(--ink);
    display:flex;flex-direction:column;align-items:center;justify-content:center;gap:4px;color:var(--white)}
  .brand__mark{width:12px;height:12px;background:var(--white)}
  .brand__name{font-weight:300;font-size:11px;letter-spacing:.2px;text-align:center;line-height:1.15}
  .brand__name span{display:block;font-size:6px;letter-spacing:.3px}

  .kicker{font-size:7.5px;font-weight:700;letter-spacing:3px;text-transform:uppercase;text-align:center;width:100%}
  .headline{font-size:21px;line-height:25px;font-weight:400;text-align:center;width:100%;text-transform:uppercase}
  .headline b{font-weight:900}
  .tagbar{background:var(--ink);color:var(--white);font-size:6px;font-weight:700;text-align:center;line-height:14px;width:190px;left:65px}

  .footer{position:absolute;left:0;bottom:0;width:100%;height:13px;background:var(--ink);color:var(--white);
    display:flex;justify-content:space-between;align-items:center;padding:0 12px;font-size:4.3px;font-weight:700;letter-spacing:1.6px;text-transform:uppercase}

  .eyebrow{font-size:5.5px;font-weight:700;letter-spacing:2.4px;text-transform:uppercase;text-decoration:underline}
  .title-gold{color:var(--gold);font-weight:900;font-size:18px;line-height:22px;text-transform:uppercase}
  .sub-gold{color:var(--gold);font-size:10px;font-weight:700}

  .gold-band{position:absolute;left:0;top:128px;width:100%;height:195px;background:var(--gold);padding:24px 42px 0}
  .lead{font-size:10.5px;font-weight:700;line-height:13px}
  .checks{list-style:none;margin-top:10px}
  .checks li{display:flex;align-items:center;gap:9px;font-size:10px;height:25px}
  .checks svg{width:9px;height:8px;flex:none}
  .body-copy{font-size:7.2px;line-height:9px;margin-top:8px}
  .body-strong{font-size:7.2px;font-weight:700;margin-top:9px}

  .benefit-box{position:absolute;left:42px;top:351px;width:58px;height:58px;background:var(--ink);color:var(--white);
    font-size:10px;line-height:13px;padding:14px 0 0 10px}
  .benefits{position:absolute;left:113px;top:354px;list-style:none}
  .benefits li{display:flex;align-items:center;gap:6px;font-size:9.5px;font-weight:700;height:18.5px}
  .benefits svg{width:9px;height:8px}

  .contact-top{position:absolute;left:0;top:0;width:100%;height:95px;background:var(--gold);clip-path:polygon(0 0,100% 0,100% 48px,0 95px)}
  .contact-cols{position:absolute;top:196px;font-size:5.6px;line-height:6.8px;text-transform:uppercase}
  .contact-cols .lbl{font-weight:700;text-decoration:underline}
  .contact-cols p{margin-bottom:7px}
  .closing{position:absolute;left:0;top:272px;width:100%;height:180px;background:var(--ink);color:var(--white);
    clip-path:polygon(0 45px,100% 0,100% 100%,0 100%)}
</style>
</head>
<body>

<section class="page page--cover">
  <div class="hero-photo" role="img" aria-label="Fotografie: dunkler Supersportwagen driftet mit Reifenqualm auf einer Rennstrecke vor Bäumen"></div>
  <div class="brand"><div class="brand__mark"></div><div class="brand__name">VELOURA CARS<span>LUXURY CAR RENTAL</span></div></div>
  <div class="abs kicker" style="top:326px">Flexibilität trifft Luxus</div>
  <div class="abs headline" style="top:342px">Jetzt den <b>Traum</b> vom<br><b>PS-Monster</b> erfüllen!</div>
  <div class="abs tagbar" style="top:403px">MIT NUR 35% ANZAHLUNG UND OHNE KREVAG!</div>
  <footer class="footer"><span>Veloura Cars® Luxury Car Rental ©</span><span>www.pk-mobil.de</span></footer>
</section>

<section class="page page--info">
  <div class="abs eyebrow" style="left:42px;top:40px">Veloura Cars® Luxury Car Rental ©</div>
  <div class="abs title-gold" style="left:42px;top:52px">Jetzt Wunschauto<br>sichern</div>
  <div class="abs sub-gold" style="left:42px;top:98px">mit nur 35% Anzahlung und OHNE KREVAG!</div>
  <div class="gold-band">
    <div class="lead">Sie wählen das Fahrzeug aus<br>&nbsp;– wir übernehmen den Ankauf.</div>
    <ul class="checks">
      <li><svg viewBox="0 0 10 8"><polyline points="1,4 4,7 9,1" fill="none" stroke="#1b1b1b" stroke-width="1.6"/></svg>Anzahlung von 35%</li>
      <li><svg viewBox="0 0 10 8"><polyline points="1,4 4,7 9,1" fill="none" stroke="#1b1b1b" stroke-width="1.6"/></svg>Ohne KREVAG-Prüfung</li>
      <li><svg viewBox="0 0 10 8"><polyline points="1,4 4,7 9,1" fill="none" stroke="#1b1b1b" stroke-width="1.6"/></svg>Nach 2 Jahren zum Restwert übernehmen</li>
    </ul>
    <p class="body-copy">Unsere fairen Monatstarife ermöglichen es Dir, den Sportwagen Deiner Träume Tag für Tag zu erleben, ohne dass Dich finanzielle Gründe daran hindern könnten.</p>
    <p class="body-strong">Jetzt Traumauto mieten und Fahrspaß der Luxusklasse genießen!</p>
  </div>
  <div class="benefit-box">Deine<br>Vorteile</div>
  <ul class="benefits">
    <li><svg viewBox="0 0 10 8"><polyline points="1,4 4,7 9,1" fill="none" stroke="#1b1b1b" stroke-width="1.8"/></svg>faire Monatstarife</li>
    <li><svg viewBox="0 0 10 8"><polyline points="1,4 4,7 9,1" fill="none" stroke="#1b1b1b" stroke-width="1.8"/></svg>Vollkaskoversicherung</li>
    <li><svg viewBox="0 0 10 8"><polyline points="1,4 4,7 9,1" fill="none" stroke="#1b1b1b" stroke-width="1.8"/></svg>24/7 freundlichen Kundenservice</li>
  </ul>
  <footer class="footer"><span>Veloura Cars® Luxury Car Rental ©</span><span>www.pk-mobil.de</span></footer>
</section>

<section class="page page--contact">
  <div class="contact-top"></div>
  <div class="brand"><div class="brand__mark"></div><div class="brand__name">VELOURA CARS<span>LUXURY CAR RENTAL</span></div></div>
  <div class="abs eyebrow" style="left:42px;top:139px;color:var(--gold);text-decoration:none;font-weight:400">Veloura Cars® Luxury Car Rental ©</div>
  <div class="abs title-gold" style="left:42px;top:150px;font-size:18px">Kontaktiere uns!</div>
  <div class="contact-cols" style="left:30px">
    <p class="lbl" style="text-decoration:underline;font-weight:700">Montags bis Freitags von 09:00 Uhr bis 19:00 Uhr,<br>am Wochenende von 09:00 Uhr bis 15:00 Uhr</p>
    <p>+49 (0)30 555 018 240<br>+49 (0)30 555 018 240</p>
    <p class="lbl">24h-Notfall-Hotline</p>
    <p>+49 (0)30 / 555 018 241</p>
  </div>
  <div class="contact-cols" style="left:191px">
    <p class="lbl">E-Mail</p>
    <p>nuvolk@pk-mobil.de</p>
    <p class="lbl">Postadresse</p>
    <p>Veloura Cars GmbH<br>Lindenallee 14<br>81479 Musterbach</p>
  </div>
  <div class="closing">
    <div class="abs kicker" style="top:62px">Flexibilität trifft Luxus</div>
    <div class="abs headline" style="top:77px">Jetzt den <b>Traum</b> vom<br><b>PS-Monster</b> erfüllen!</div>
    <div class="abs" style="top:137px;width:100%;text-align:center;font-size:6px;font-weight:700">MIT NUR 35% ANZAHLUNG UND OHNE KREVAG!</div>
  </div>
  <footer class="footer"><span>Veloura Cars® Luxury Car Rental ©</span><span>www.pk-mobil.de</span></footer>
</section>

</body>
</html>
```